Talvex - Fiber Internet to the home postcard

Design a postcard for my company, Talvex, using the logo below. On the front of the card:
- No Buffering • No BS
- Second line should be the logo
- $60 / month • 10-Gigs
- talvexfiber.net

Color palate should follow the colors in the logo.

Address should say
- Special pricing during construction
- Our best price
- Our fastest speed
- $60 / month • 10-Gigs
- talvexfiber.net

Target Market(s)

25 - 55 year olds. Middle income/class. People with kids and pick up trucks

Industry/Entity Type

Fiber Internet Service Provider

Font styles to use
Sans Serif

Colors

Designer to choose colors to be used in the design.

Requirements
Nice to have
• I am open to more creative changes

```html
<!DOCTYPE html>
<html lang="en">
<head>
<meta charset="utf-8">
<title>Talvex – Fiber Internet Postcard</title>
<link rel="stylesheet" href="https://fonts.googleapis.com/css2?family=Montserrat:wght@600;700;800;900&display=swap">
<style>
  :root {
    --navy: #1b2a5c;
    --green: #7ac143;
    --white: #ffffff;
    --backdrop: #5b5b5b;
    --fiber-light: #4f86c9;
  }
  * { box-sizing: border-box; margin: 0; padding: 0; }
  html, body { width: 1000px; height: 1200px; overflow: hidden; }
  body {
    background: var(--backdrop);
    font-family: "Montserrat", Arial, sans-serif;
    position: relative;
  }
  .postcard {
    position: absolute;
    left: 206px;
    width: 588px;
    height: 456px;
    overflow: hidden;
    box-shadow: 4px 6px 10px rgba(0,0,0,0.45);
  }
  .postcard--front { top: 107px; background: var(--navy); }
  .postcard--back { top: 662px; background: var(--white); }
  .artwork { position: absolute; inset: 0; width: 588px; height: 456px; }
  .card-item { position: absolute; line-height: 1; }

  /* Front */
  .postcard .tagline-box {
    left: 43px; top: 29px; width: 504px; height: 44px;
    border: 1.5px solid var(--white); border-radius: 8px;
    display: flex; align-items: center; justify-content: center;
    color: var(--white); font-weight: 600; font-size: 35px; letter-spacing: 0.5px;
  }
  .tagline-box .dot { color: var(--green); margin: 0 14px; font-size: 26px; }
  .postcard .brand {
    left: 40px; top: 99px;
    color: var(--white); font-weight: 900; font-size: 74px; letter-spacing: -2px;
  }
  .postcard .price { left: 41px; top: 194px; color: var(--white); font-weight: 900; font-size: 43px; letter-spacing: -1px; }
  .price .slash { color: var(--green); margin: 0 3px; }
  .postcard .speed { left: 41px; top: 241px; color: var(--white); font-weight: 900; font-size: 43px; letter-spacing: -1px; }
  .postcard .web-address {
    right: 37px; color: var(--navy); font-weight: 900; font-size: 50px; letter-spacing: -2px;
  }
  .postcard--front .web-address { top: 347px; }
  .postcard .closing-line {
    left: 42px; color: var(--white); font-weight: 700; letter-spacing: 0.4px;
  }
  .postcard--front .closing-line { top: 410px; font-size: 22.5px; }

  /* Back */
  .postcard .question-panel {
    left: 0; top: 161px; width: 313px; height: 84px;
    background: var(--green); border-radius: 0 10px 10px 0;
    padding: 8px 0 0 56px;
    color: var(--white); font-weight: 900; font-size: 18px; line-height: 23px; letter-spacing: -0.3px;
  }
  .postcard .offer-list {
    left: 56px; top: 254px; list-style: none;
    color: var(--navy); font-weight: 700; font-size: 14px; line-height: 17px;
  }
  .postcard .stamp-box {
    left: 453px; top: 44px; width: 89px; height: 88px;
    border: 1.5px solid var(--navy);
  }
  .postcard--back .web-address { top: 350px; }
  .postcard--back .closing-line { top: 410px; font-size: 25px; }
</style>
</head>
<body>

<section class="postcard postcard--front" aria-label="Postcard front">
  <svg class="artwork" viewBox="0 0 588 456">
    <defs>
      <radialGradient id="fiberGlow" cx="0.85" cy="0.35" r="0.75">
        <stop offset="0" stop-color="#cfe3ff"/>
        <stop offset="0.25" stop-color="#4f86c9"/>
        <stop offset="0.7" stop-color="#244a8e" stop-opacity="0.6"/>
        <stop offset="1" stop-color="#1b2a5c" stop-opacity="0"/>
      </radialGradient>
    </defs>
    <rect x="290" y="0" width="298" height="340" fill="url(#fiberGlow)" role="img" aria-label="Photo of glowing fiber optic strands fanning out"/>
    <path d="M0 339 C40 355 80 367 114 367 C230 367 380 305 480 305 C530 305 565 322 588 336 L588 456 L0 456 Z" fill="#7ac143"/>
    <path d="M0 295 C50 320 110 330 180 326 C300 318 400 272 588 300" fill="none" stroke="#7ac143" stroke-width="4"/>
    <path d="M0 310 C60 333 130 338 200 334 C320 325 420 282 588 312" fill="none" stroke="#7ac143" stroke-width="3"/>
    <path d="M0 327 C40 342 80 350 114 350 C240 350 390 256 491 256 C540 256 568 270 588 282" fill="none" stroke="#ffffff" stroke-width="3.5"/>
  </svg>
  <div class="card-item tagline-box">No Buffering<span class="dot">●</span>No BS</div>
  <div class="card-item brand">Talvex</div>
  <div class="card-item price">$60<span class="slash">/</span>month</div>
  <div class="card-item speed">10-Gigs</div>
  <div class="card-item web-address">talvexfiber.net</div>
  <p class="card-item closing-line">You deserve a better internet experience.</p>
</section>

<section class="postcard postcard--back" aria-label="Postcard back">
  <svg class="artwork" viewBox="0 0 588 456">
    <defs>
      <linearGradient id="homesTone" x1="0" y1="0" x2="1" y2="1">
        <stop offset="0" stop-color="#8a8d90"/>
        <stop offset="1" stop-color="#f2f3f4"/>
      </linearGradient>
    </defs>
    <rect x="71" y="43" width="220" height="118" fill="url(#homesTone)" role="img" aria-label="Illustration of three metallic houses connected by a yellow fiber optic cable"/>
    <path d="M0 338 C40 358 80 370 114 370 C230 370 370 306 469 306 C520 306 560 322 588 338 L588 456 L0 456 Z" fill="#7ac143"/>
  </svg>
  <div class="card-item stamp-box" aria-label="Stamp area"></div>
  <div class="card-item question-panel">Looking for a high speed<br>internet solution<br>for your home?</div>
  <ul class="card-item offer-list">
    <li>Special Pricing During Construction</li>
    <li>Our best price</li>
    <li>Our fastest speed</li>
    <li>$60 / month · 10-Gigs</li>
    <li>talvexfiber.net</li>
  </ul>
  <div class="card-item web-address">talvexfiber.net</div>
  <p class="card-item closing-line">The fast affordable internet you need</p>
</section>

</body>
</html>
```